Akademie für Lichtwegkunde
Zielgruppe
Ich biete die beiden Seminare 'Kraftquell am Werktag' und 'Feinsinn am Werktag' an. Die Zielgruppe sind spirituell interessierte Leute.
Aufgabenstellung
Die Anzeige sollte mehr oder weniger mit den Farben meiner Webseite übereinstimmen (www.sonnenpfad-raum.ch).
Grösse der Anzeige:
breit: 121mm
hoch: 124mm
Die Anzeige sollte mein persönliches Bild und das Logo enthalten.
Text:
Feinsinn am Werktag:
Seminare zur Förderung Ihrer Intuition. Entdecken Sie Ihre eigene Medialität und lernen Sie diese gezielt im Alltag einzusetzen.
26./27. August 2017
11./12. November 2017
Kraftquell am Werktag:
Seminare für energetisches Heilen. Lernen Sie sich und andere Menschen energetisch zu begleiten.
16./17. September 2017
9./10. Dezember 2017
2 für 1 - Aktion:
Kommen Sie zu zweit und bezahlen Sie nur für eine Person
(gültig bis Ende 2017)
Webseite:
www.sonnenpfad-raum.ch
Seminarort: Grünholdau, 3286 Lorbachtal, Schweiz

```html
<!DOCTYPE html>
<html lang="de">
<head>
<meta charset="utf-8">
<title>Akademie für Lichtwegkunde – Seminaranzeige</title>
<link href="https://fonts.googleapis.com/css2?family=Nunito+Sans:wght@400;700;800&display=swap" rel="stylesheet">
<style>
  :root {
    --page-bg: #d9d9d9;
    --paper: #ffffff;
    --brand-blue: #3f7fc0;
    --band-blue: #6693cf;
    --offer-blue: #5086c6;
    --accent-orange: #e0701e;
    --ink: #2b2b2b;
    --white: #ffffff;
  }
  * { margin: 0; padding: 0; box-sizing: border-box; }
  html, body {
    width: 1200px; height: 801px; overflow: hidden;
    background: var(--page-bg);
    font-family: "Nunito Sans", Arial, sans-serif;
  }
  .ad {
    position: absolute; left: 229px; top: 20px;
    width: 742px; height: 760px;
    background: var(--paper);
    overflow: hidden;
  }
  .portrait {
    position: absolute; left: 0; top: 0; width: 193px; height: 172px;
    background: radial-gradient(ellipse at 55% 55%, #9a9a9a 0%, #5e5e5e 55%, #3a3a3a 100%);
  }
  .brand {
    position: absolute; right: 40px; top: 62px;
    display: flex; align-items: center; gap: 12px;
    font-size: 27px; font-weight: 700; color: var(--brand-blue);
  }
  .brand-dot { width: 22px; height: 22px; border-radius: 50%; background: var(--accent-orange); }
  .top-band {
    position: absolute; left: 0; top: 172px; width: 100%; height: 15px;
    background: var(--band-blue);
  }
  .seminar { position: absolute; top: 233px; width: 330px; }
  .seminar--intuition { left: 37px; }
  .seminar--healing { left: 389px; }
  .seminar-kicker { font-size: 19px; color: var(--brand-blue); line-height: 24px; }
  .seminar-title {
    font-size: 25px; font-weight: 700; color: var(--accent-orange);
    line-height: 32px; margin-top: 2px;
  }
  .seminar-text, .seminar-dates {
    font-size: 18.5px; color: var(--ink); line-height: 26px;
  }
  .seminar-text { margin-top: 24px; height: 78px; }
  .seminar-dates { margin-top: 24px; }
  .venue {
    position: absolute; left: 37px; right: 37px; top: 560px;
    display: flex; justify-content: space-between;
    font-size: 18.5px; color: var(--ink);
  }
  .venue-url { color: var(--accent-orange); font-weight: 700; }
  .offer {
    position: absolute; left: 0; top: 588px; width: 742px; height: 172px;
    background: var(--offer-blue); color: var(--white);
  }
  .offer-kicker { position: absolute; left: 37px; top: 30px; font-size: 25px; }
  .offer-headline {
    position: absolute; left: 37px; top: 64px;
    font-size: 32px; font-weight: 800; line-height: 39px;
  }
  .offer-ribbon { position: absolute; left: 0; top: 0; }
</style>
</head>
<body>
  <section class="ad">
    <div class="portrait" role="img" aria-label="Schwarzweiss-Porträt des Seminarleiters"></div>
    <div class="brand"><span class="brand-dot"></span><span class="brand-name">Akademie für Lichtwegkunde</span></div>
    <div class="top-band"></div>

    <article class="seminar seminar--intuition">
      <p class="seminar-kicker">Feinsinn am Werktag</p>
      <h2 class="seminar-title">Seminar zur Förderung<br>Ihrer Intuition</h2>
      <p class="seminar-text">Entdecken Sie Ihre eigene<br>Medialität und lernen Sie diese<br>gezielt im Alltag einzusetzen.</p>
      <p class="seminar-dates">26. bis 27. August 2017<br>11. bis 12. November 2017</p>
    </article>

    <article class="seminar seminar--healing">
      <p class="seminar-kicker">Kraftquell am Werktag</p>
      <h2 class="seminar-title">Seminar für<br>energetisches Heilen</h2>
      <p class="seminar-text">Lernen Sie sich und andere<br>Menschen energetisch zu<br>begleiten.</p>
      <p class="seminar-dates">16. bis 17. September 2017<br>9. bis 10. Dezember 2017</p>
    </article>

    <p class="venue"><span>Seminarort: Grünholdau, 3286 Lorbachtal, Schweiz</span><span class="venue-url">www.sonnenpfad-raum.ch</span></p>

    <section class="offer">
      <svg class="offer-ribbon" width="742" height="172" viewBox="0 0 742 172">
        <polygon points="590,0 662,0 742,80 742,152" fill="#ffffff"/>
        <text x="690" y="66" transform="rotate(45 690 66)" text-anchor="middle"
              font-family="Nunito Sans, Arial, sans-serif" font-size="25" font-weight="800" fill="#3f7fc0">Aktion</text>
        <text x="650" y="102" transform="rotate(45 650 102)" text-anchor="middle"
              font-family="Nunito Sans, Arial, sans-serif" font-size="12.5" fill="#ffffff">gültig bis 31.12.2017</text>
      </svg>
      <p class="offer-kicker">2 für 1</p>
      <p class="offer-headline">Kommen Sie zu zweit und<br>bezahlen Sie nur für eine Person</p>
    </section>
  </section>
</body>
</html>
```